Personal Training, Nutrition and Habit Change

I am looking to create a memorable brand name and logo that describes what I offer..something like, "Red Maple Crew" or "Harbor Stone Fitness". I want people to know that they can come to me to elevate their lives through a balance of fitness, good nutrition and mental well-being through meditating, mindfulness and a program of stress relief.

Target Market(s)

Well established individuals who are interested in spending money for their health and well-being and making a long term commitment to themselves.

Industry/Entity Type

Fitness

Contact Information for Business Card

Would like a horizontal card, possibly in black with blue and white lettering with the logo that implies a figure running, moving fast or is agile. Would like a statement on the back about habit change and importance of fitness

Logo Text

Create A Stronger Healthier You or Elevate Your Life and Well Being

Font styles to use
Sans Serif

Colors

Designer to choose colors to be used in the design.

Requirements
Must have
• A strong, powerful name (brand) for my company. Something short, powerful, memorable and relevant. A company motto that describes briefly what I'll help clients achieve, i.e. Create a Stronger Healthier You, etc. A place for my name and multiple credentials with room for contact info of course. On the back, does it make practical sense to describe habit change, achieving balance making commitment to one's health and well being and finding great joy in one's daily life.
Nice to have
• Basically what I said above.
Should not have
• Just show me what you've got!

```html
<!DOCTYPE html>
<html lang="en">
<head>
<meta charset="utf-8">
<title>Harbor Stone Fitness – Business Card</title>
<link rel="stylesheet" href="https://fonts.googleapis.com/css2?family=Montserrat:wght@300;400;700&display=swap">
<style>
  :root {
    --backdrop: #5f5f5f;
    --card-white: #f7f7f7;
    --card-black: #1b1b1c;
    --brand-blue: #3a7bc8;
    --ink: #111111;
    --paper-text: #ffffff;
  }
  * { box-sizing: border-box; margin: 0; padding: 0; }
  html, body {
    width: 1200px; height: 900px; overflow: hidden;
    background: var(--backdrop);
    font-family: "Montserrat", Arial, sans-serif;
  }
  .stage {
    width: 1200px; height: 900px;
    display: flex; align-items: center; justify-content: center; gap: 40px;
  }
  .card {
    position: relative;
    width: 540px; height: 310px;
    border-radius: 24px;
    overflow: hidden;
    box-shadow: 0 14px 30px rgba(0,0,0,0.35);
  }
  .card--front { background: var(--card-white); }
  .card--back { background: var(--card-black); }

  .brand { display: flex; align-items: center; gap: 10px; }
  .brand__dot { width: 22px; height: 22px; border-radius: 50%; background: var(--brand-blue); flex: none; }
  .brand__name { font-weight: 700; text-transform: uppercase; letter-spacing: 0.04em; }

  .card--front .brand { position: absolute; left: 32px; top: 30px; }
  .card--front .brand__name { font-size: 21px; color: var(--ink); }

  .holder { position: absolute; left: 40px; top: 100px; }
  .holder__name { font-size: 24px; font-weight: 300; color: var(--ink); letter-spacing: 0.02em; }
  .holder__title { font-size: 14px; font-weight: 300; color: var(--brand-blue); margin-top: 2px; }

  .contact { position: absolute; left: 40px; top: 195px; list-style: none; }
  .contact__item {
    display: flex; align-items: center; gap: 10px;
    font-size: 14px; font-weight: 400; color: var(--ink); margin-bottom: 9px;
  }
  .contact__item--web { color: var(--brand-blue); }
  .contact__icon { width: 14px; height: 14px; flex: none; }

  .accent-circle {
    position: absolute; right: -90px; bottom: -120px;
    width: 330px; height: 330px; border-radius: 50%;
    background: var(--brand-blue);
  }

  .card--back .brand {
    position: absolute; left: 0; right: 0; top: 118px; justify-content: center;
  }
  .card--back .brand__dot { width: 26px; height: 26px; }
  .card--back .brand__name { font-size: 26px; color: var(--paper-text); }
  .tagline {
    position: absolute; left: 0; right: 0; top: 180px; text-align: center;
    font-size: 15px; font-weight: 300; color: var(--paper-text); letter-spacing: 0.03em;
  }
  .tagline__accent { color: var(--brand-blue); }
</style>
</head>
<body>
<main class="stage">
  <section class="card card--front" aria-label="Card front">
    <div class="brand">
      <span class="brand__dot"></span>
      <span class="brand__name">Harbor Stone Fitness</span>
    </div>
    <div class="holder">
      <p class="holder__name">YOUR NAME</p>
      <p class="holder__title">JOB TITLE</p>
    </div>
    <ul class="contact">
      <li class="contact__item">
        <svg class="contact__icon" viewBox="0 0 16 16"><path fill="#3a7bc8" d="M1 5c0-2 2-3 7-3s7 1 7 3v1h-4V5H5v1H1zM3 8l2-2h6l2 2v6H3z"/><circle cx="8" cy="10.5" r="1.8" fill="#f7f7f7"/></svg>
        000 000 0000
      </li>
      <li class="contact__item">
        <svg class="contact__icon" viewBox="0 0 16 16"><rect x="1" y="3" width="14" height="10" fill="#3a7bc8"/><path d="M1 3l7 6 7-6" fill="none" stroke="#f7f7f7" stroke-width="1.3"/></svg>
        youremail@xyz.com
      </li>
      <li class="contact__item contact__item--web">
        <svg class="contact__icon" viewBox="0 0 16 16" fill="none" stroke="#3a7bc8" stroke-width="1.1"><circle cx="8" cy="8" r="6.5"/><ellipse cx="8" cy="8" rx="3" ry="6.5"/><path d="M1.5 8h13M2.5 4.8h11M2.5 11.2h11"/></svg>
        www.yourwebsite.com
      </li>
    </ul>
    <div class="accent-circle"></div>
  </section>

  <section class="card card--back" aria-label="Card back">
    <div class="brand">
      <span class="brand__dot"></span>
      <span class="brand__name">Harbor Stone Fitness</span>
    </div>
    <p class="tagline">STRONGER HEALTHIER <span class="tagline__accent">YOU</span></p>
  </section>
</main>
</body>
</html>
```